New Business Card

Would like a shiny card with Metallic logo raised on th front. Address 418 Kestwick Lane, Toronto Ontario M4T2B8, phone 416 555 0382, email kmvc@lorentel.ca and web www.kmvc.ca on the back in right and left lower corners balanced. Top of back should say Personalized Care for Pet's and their People centered. Leaving space on the back to write. Horizontal placement

```html
<!DOCTYPE html>
<html lang="en">
<head>
<meta charset="utf-8">
<title>Kestwick Meadow Vet Clinic – Business Card</title>
<link href="https://fonts.googleapis.com/css2?family=Saira+Semi+Condensed:wght@400;600&display=swap" rel="stylesheet">
<style>
  :root {
    --canvas: #ffffff;
    --card: #e9e9e9;
    --ink: #1e1e1e;
    --mark: #5b5b5b;
    --icon: #555555;
    --rule: #d5d5d5;
  }
  * { margin: 0; padding: 0; box-sizing: border-box; }
  html, body {
    width: 1200px; height: 1000px; overflow: hidden;
    background: var(--canvas);
    font-family: "Saira Semi Condensed", "Arial Narrow", sans-serif;
    color: var(--ink);
  }
  .canvas { position: relative; width: 1200px; height: 1000px; }

  .card { position: absolute; background: var(--card); }
  .card--front {
    left: 60px; top: 185px; width: 360px; height: 630px;
    border-radius: 50px 0 50px 0;
  }
  .card--back {
    left: 510px; top: 321px; width: 630px; height: 359px;
    border-radius: 0 50px 0 50px;
  }

  .brand { position: absolute; left: 0; top: 105px; width: 100%; text-align: center; }
  .brand__dot {
    width: 96px; height: 96px; border-radius: 50%;
    background: var(--mark); margin: 0 auto 12px;
  }
  .brand__name {
    font-weight: 600; color: var(--ink);
    font-size: 27px; letter-spacing: 1px; line-height: 1;
  }
  .brand__sub {
    font-weight: 600; color: var(--ink);
    font-size: 13px; letter-spacing: 2px; margin-top: 4px;
  }

  .contact { position: absolute; left: 52px; top: 380px; list-style: none; }
  .contact__item {
    display: flex; align-items: flex-start;
    font-size: 21px; line-height: 26px; margin-bottom: 14px;
  }
  .contact__icon { width: 26px; height: 26px; margin-right: 18px; flex: none; }
  .contact__icon svg { width: 20px; height: 20px; margin: 3px 0 0 5px; display: block; }
  .contact__item--address .contact__icon svg { margin-top: 9px; }

  .tagline {
    position: absolute; left: 0; top: 36px; width: 100%;
    text-align: center; font-size: 28px; font-weight: 400;
  }
  .write-lines { position: absolute; left: 60px; top: 129px; width: 501px; }
  .write-lines__rule { height: 2px; background: var(--rule); margin-bottom: 45px; }
</style>
</head>
<body>
<main class="canvas">
  <section class="card card--front" aria-label="Card front">
    <div class="brand">
      <div class="brand__dot"></div>
      <div class="brand__name">KESTWICK MEADOW</div>
      <div class="brand__sub">VET CLINIC</div>
    </div>
    <ul class="contact">
      <li class="contact__item contact__item--address">
        <span class="contact__icon">
          <svg viewBox="0 0 20 20" fill="none" stroke="var(--icon)" stroke-width="1.4">
            <path d="M10 19c-4-5-6-8-6-11a6 6 0 0 1 12 0c0 3-2 6-6 11z"/>
            <circle cx="10" cy="8" r="2"/>
          </svg>
        </span>
        <span>418 Kestwick Lane,<br>Toronto Ontario M4T2B8</span>
      </li>
      <li class="contact__item">
        <span class="contact__icon">
          <svg viewBox="0 0 20 20" fill="none" stroke="var(--icon)" stroke-width="1.4" stroke-linejoin="round">
            <path d="M4 2l3 0 1.5 4-2 1.5c1 2.5 3 4.5 5.5 5.5l1.5-2 4 1.5v3c0 1-1 2-2 2C9 17.5 2.5 11 2.5 4c0-1 .5-2 1.5-2z"/>
          </svg>
        </span>
        <span>416 555 0382</span>
      </li>
      <li class="contact__item">
        <span class="contact__icon">
          <svg viewBox="0 0 20 20" fill="none" stroke="var(--icon)" stroke-width="1.4">
            <circle cx="10" cy="10" r="3"/>
            <path d="M13 7v4c0 2 3 2 3-1a6 6 0 1 0-2.5 5"/>
          </svg>
        </span>
        <span>kmvc@lorentel.ca</span>
      </li>
      <li class="contact__item">
        <span class="contact__icon">
          <svg viewBox="0 0 20 20" fill="none" stroke="var(--icon)" stroke-width="1.3">
            <circle cx="10" cy="10" r="7.5"/>
            <ellipse cx="10" cy="10" rx="3.2" ry="7.5"/>
            <path d="M2.5 10h15M3.8 6h12.4M3.8 14h12.4"/>
          </svg>
        </span>
        <span>www.kmvc.ca</span>
      </li>
    </ul>
  </section>

  <section class="card card--back" aria-label="Card back">
    <h1 class="tagline">Personalized Care for Pet's and their People</h1>
    <div class="write-lines">
      <div class="write-lines__rule"></div>
      <div class="write-lines__rule"></div>
      <div class="write-lines__rule"></div>
      <div class="write-lines__rule"></div>
      <div class="write-lines__rule"></div>
    </div>
  </section>
</main>
</body>
</html>
```